K&T Holdings

Design a modern simple business card. I have attached a clean version of a card we like form Marrowfield Partners another company we own. I also attached the old K&T card design and logo and a couple of ideas we had but just can't finalize on whether we like them or not. We would like to include the 20 year logo somewhere on the card.

```html
<!DOCTYPE html>
<html lang="en">
<head>
<meta charset="utf-8">
<title>K&amp;T Holdings – Business Card</title>
<link rel="stylesheet" href="https://fonts.googleapis.com/css2?family=Open+Sans:wght@400;600;700&amp;family=Montserrat:wght@500;600&amp;display=swap">
<style>
  :root {
    --navy: #29275f;
    --grey: #808080;
    --grey-soft: #8c8c8c;
    --ink: #1c1c1c;
    --paper: #ffffff;
    --stage: #232323;
  }
  * { box-sizing: border-box; margin: 0; padding: 0; }
  html, body {
    width: 1200px; height: 780px; overflow: hidden;
    background: var(--stage);
    font-family: "Open Sans", Arial, sans-serif;
  }
  .canvas {
    position: relative; width: 1200px; height: 780px;
    display: flex; align-items: center; justify-content: center; gap: 40px;
  }
  .card {
    position: relative; width: 540px; height: 309px; overflow: hidden;
  }

  /* Front */
  .card-front { background: var(--paper); color: var(--ink); }
  .brand {
    position: absolute; left: 34px; top: 22px;
    display: flex; align-items: center; gap: 10px;
    color: var(--navy); font-weight: 700; font-size: 38px; line-height: 1;
  }
  .brand-dot {
    width: 16px; height: 16px; border-radius: 50%; background: var(--navy);
  }
  .contact { position: absolute; left: 34px; top: 86px; }
  .contact-name {
    color: var(--navy); font-weight: 700; font-size: 22px; letter-spacing: .3px;
  }
  .contact-title { font-size: 12px; margin-top: 1px; }
  .contact-address { font-size: 12px; line-height: 1.45; margin-top: 10px; }
  .contact-lines { list-style: none; margin-top: 8px; font-size: 12px; line-height: 1.6; }
  .contact-lines li { display: flex; align-items: center; gap: 7px; }
  .contact-lines svg { width: 11px; height: 11px; fill: var(--navy); flex: none; }

  .services {
    position: absolute; right: 22px; top: 26px;
    display: flex; align-items: flex-start; gap: 6px;
  }
  .services-list { list-style: none; text-align: right; font-size: 12.5px; line-height: 1.55; }
  .services-list li::after {
    content: ""; display: inline-block; width: 7px; height: 7px; border-radius: 50%;
    background: var(--navy); margin-left: 8px; vertical-align: middle;
  }
  .services-label {
    writing-mode: vertical-rl; color: var(--navy);
    font-family: "Montserrat", Arial, sans-serif; font-weight: 600;
    font-size: 12px; letter-spacing: 3px; margin-top: 2px;
  }

  .anniversary {
    position: absolute; right: 30px; bottom: 14px;
    display: grid; grid-template-columns: auto auto; align-items: end;
  }
  .anniversary-number {
    color: var(--navy); font-family: "Montserrat", Arial, sans-serif;
    font-weight: 600; font-size: 118px; line-height: .82; letter-spacing: -4px;
  }
  .anniversary-years {
    writing-mode: vertical-rl; color: var(--grey-soft);
    font-family: "Montserrat", Arial, sans-serif; font-weight: 500;
    font-size: 15px; letter-spacing: 3px; margin-left: 4px;
  }
  .anniversary-span {
    grid-column: 1 / 3; color: var(--grey-soft);
    font-family: "Montserrat", Arial, sans-serif; font-weight: 500;
    font-size: 22px; letter-spacing: 1px; margin-top: 6px;
  }

  /* Back */
  .card-back {
    background: var(--grey);
    display: flex; align-items: center; justify-content: center; gap: 16px;
    color: var(--paper); font-weight: 700; font-size: 84px; line-height: 1;
  }
  .card-back .brand-dot { width: 30px; height: 30px; background: var(--paper); }
</style>
</head>
<body>
<main class="canvas">
  <section class="card card-front" aria-label="Business card front">
    <div class="brand"><span>K&amp;T</span><span class="brand-dot"></span></div>

    <div class="contact">
      <h1 class="contact-name">DANA WHITLOCK</h1>
      <p class="contact-title">IT Director</p>
      <p class="contact-address">Corporate: 118 Harbor Lane,<br>Suite 402, Lakeview, TX 75010</p>
      <ul class="contact-lines">
        <li>
          <svg viewBox="0 0 24 24" aria-hidden="true"><path d="M6.6 10.8a15.1 15.1 0 0 0 6.6 6.6l2.2-2.2a1 1 0 0 1 1-.25 11.4 11.4 0 0 0 3.6.57 1 1 0 0 1 1 1V20a1 1 0 0 1-1 1A17 17 0 0 1 3 4a1 1 0 0 1 1-1h3.5a1 1 0 0 1 1 1c0 1.25.2 2.45.57 3.57a1 1 0 0 1-.25 1z"/></svg>
          555-201-4470
        </li>
        <li>
          <svg viewBox="0 0 24 24" aria-hidden="true"><path d="M7 1h10a2 2 0 0 1 2 2v18a2 2 0 0 1-2 2H7a2 2 0 0 1-2-2V3a2 2 0 0 1 2-2zm0 3v14h10V4z"/></svg>
          555-318-2096
        </li>
        <li>
          <svg viewBox="0 0 24 24" aria-hidden="true"><path d="M2 5h20v14H2zm2 2v.5l8 5 8-5V7zm0 2.8V17h16V9.8l-8 5z"/></svg>
          dwhitlock@ktholdings.com
        </li>
      </ul>
    </div>

    <div class="services">
      <ul class="services-list">
        <li>I&amp;E</li>
        <li>Rotating</li>
        <li>Fabrication</li>
        <li>Mechanical/Civil</li>
        <li>Heat Transfer Equipment</li>
      </ul>
      <span class="services-label">SERVICES</span>
    </div>

    <div class="anniversary">
      <span class="anniversary-number">20</span>
      <span class="anniversary-years">YEARS</span>
      <span class="anniversary-span">2004-2024</span>
    </div>
  </section>

  <section class="card card-back" aria-label="Business card back">
    <span>K&amp;T</span><span class="brand-dot"></span>
  </section>
</main>
</body>
</html>
```